Advertisement insert for magazine

Create a 5 X 4.75 advertisement for a magazine. Design must catch the eye of the reader and properly represent our brand. This will be in LANTERN magazine a local affluent magazine.

The goal of this advertisement is to represent a progressive firm with an amazing portfolio.

Target Market(s)

local businesses and business leaders of Florida.

Industry/Entity Type

Architecture

Font styles to use
Other font styles liked:
• Calibri, Calibri light

Requirements
Must have
• Modern Progressive Design. Our logo, our address and telephone number and our project images we have attached.
Should not have
• I have attached the ad from last year, we DO NOT want to replicate this ad, however this should give you an idea of the size and overall goal of the advertisement.
• (SEE LANTERN MAGAZINE KTW PDF)

```html
<!DOCTYPE html>
<html lang="en">
<head>
<meta charset="utf-8">
<title>Harrow Vale + Partners — Magazine Advertisement</title>
<link href="https://fonts.googleapis.com/css2?family=Carlito:wght@400;700&display=swap" rel="stylesheet">
<style>
  :root {
    --page: #f2f2f2;
    --ad-bg: #ffffff;
    --brand-blue: #1b7cc3;
    --text-blue: #1f6db0;
    --ink-gray: #5c5c5f;
    --panel-light: #ececee;
    --panel-dark: #c6c6c9;
    --footer-bg: #e8e8e9;
    --frame-gray: #9a9a9d;
    --divider: #2c6fa8;
  }
  * { box-sizing: border-box; margin: 0; padding: 0; }
  html, body {
    width: 1200px; height: 616px; overflow: hidden;
    background: var(--page);
    font-family: "Carlito", "Calibri", sans-serif;
  }
  .canvas { position: relative; width: 1200px; height: 616px; }
  .ad {
    position: absolute; left: 285px; top: 8px;
    width: 600px; height: 570px;
    transform: scale(1.05); transform-origin: top left;
    background: var(--ad-bg);
    border: 1px solid var(--brand-blue);
    overflow: hidden;
  }
  .feature-panel { position: absolute; left: 0; top: 0; width: 340px; height: 372px; }

  .photo {
    position: absolute;
    border: 2px solid #fff;
    outline: 1px solid var(--frame-gray);
  }
  .photo--hardware-store { left: 70px; top: 19px; width: 203px; height: 104px;
    background: linear-gradient(180deg, #2f4f8f 0%, #5d7fbf 30%, #9fb4d8 48%, #e8c88a 58%, #6b6462 72%, #3c3d42 100%); }
  .photo--residential-entry { left: 70px; top: 135px; width: 203px; height: 105px;
    background: linear-gradient(180deg, #7f9fd0 0%, #b9c3d9 30%, #6f7f96 52%, #3e5246 72%, #e0b46a 82%, #3a3a3e 100%); }
  .photo--historic-hotel { left: 70px; top: 249px; width: 203px; height: 106px;
    background: linear-gradient(180deg, #9e8fc6 0%, #e3a9b8 28%, #d9a877 48%, #b98552 66%, #e9c36a 74%, #4c4a4c 100%); }
  .photo--lounge-interior { left: 328px; top: 140px; width: 120px; height: 120px;
    background: linear-gradient(180deg, #f1ede6 0%, #d9e4ea 30%, #86b8d8 48%, #2d5fa5 64%, #b78b5a 80%, #e4dccd 100%); }
  .photo--bar-interior { left: 458px; top: 140px; width: 120px; height: 120px;
    background: linear-gradient(180deg, #2f6e7c 0%, #5c9ea6 32%, #d6c8ad 52%, #9a6b44 66%, #2e3550 84%, #c9b48e 100%); }
  .photo--car-showroom { left: 328px; top: 269px; width: 250px; height: 80px;
    background: linear-gradient(180deg, #9bb3dc 0%, #d8d3d8 35%, #eae6e0 50%, #5f6a5e 64%, #585a60 80%, #767779 100%); }

  .logo { position: absolute; left: 347px; top: 45px; width: 230px; height: 66px; }
  .logo__mark {
    position: absolute; left: 0; top: 2px; width: 46px; height: 46px;
    border-radius: 50%; background: var(--brand-blue);
  }
  .logo__name {
    position: absolute; left: 52px; top: 8px;
    font-size: 23px; font-weight: 400; letter-spacing: 0.4px; line-height: 1;
    color: var(--ink-gray); white-space: nowrap;
  }
  .logo__partners {
    position: absolute; left: 164px; top: 33px;
    font-size: 7px; letter-spacing: 1.8px; line-height: 1; color: var(--ink-gray);
  }
  .logo__services {
    position: absolute; left: 63px; top: 55px;
    font-size: 7px; letter-spacing: 1.1px; line-height: 1; color: var(--ink-gray); white-space: nowrap;
  }

  .portfolio-band {
    position: absolute; left: 0; top: 371px; width: 600px; height: 152px;
    background: var(--brand-blue);
  }
  .portfolio-band .photo { top: 12px; width: 134px; height: 128px; outline-color: #fff; }
  .photo--atrium-stair { left: 12px;
    background: linear-gradient(90deg, #f4f2ee 0%, #e6e2da 40%, #cfcac2 60%, #5e5d60 75%, #eeece8 100%); }
  .photo--waterfront-condo { left: 158px;
    background: linear-gradient(180deg, #4f8fd6 0%, #a9cbea 28%, #eef0f2 50%, #c9ced6 66%, #d25584 80%, #3f7a3c 100%); }
  .photo--office-lounge { left: 306px;
    background: linear-gradient(180deg, #c9c6c2 0%, #ecebe8 30%, #9aa3ab 45%, #5f6066 62%, #b88e6f 78%, #d9d3ca 100%); }
  .photo--spanish-lobby { left: 453px;
    background: linear-gradient(180deg, #6d3f24 0%, #9c6a43 28%, #e1d6c2 46%, #8b5d3b 66%, #a44a3c 80%, #4d2f22 100%); }

  .contact-bar {
    position: absolute; left: 0; top: 523px; width: 600px; height: 47px;
    background: var(--footer-bg);
    display: flex; align-items: center; justify-content: center;
    color: var(--text-blue);
  }
  .contact-bar__item { font-size: 13px; padding: 0 17px; white-space: nowrap; line-height: 1; }
  .contact-bar__item--phone { font-size: 16px; font-weight: 700; }
  .contact-bar__divider { width: 1.5px; height: 30px; background: var(--divider); }
</style>
</head>
<body>
<main class="canvas">
  <section class="ad" aria-label="Harrow Vale + Partners magazine advertisement">
    <svg class="feature-panel" viewBox="0 0 340 372" aria-hidden="true">
      <defs>
        <linearGradient id="panelShade" x1="0" x2="1" y1="0" y2="0">
          <stop offset="0" stop-color="#c6c6c9"/>
          <stop offset="0.5" stop-color="#ececee"/>
          <stop offset="1" stop-color="#c6c6c9"/>
        </linearGradient>
      </defs>
      <path d="M24 0 L316 0 C292 120 292 260 316 372 L24 372 C48 260 48 120 24 0 Z" fill="url(#panelShade)"/>
    </svg>

    <div class="photo photo--hardware-store" role="img" aria-label="Photo: modern two-storey glass-fronted hardware store lit at dusk"></div>
    <div class="photo photo--residential-entry" role="img" aria-label="Photo: residential tower porte-cochère entrance with palms at twilight"></div>
    <div class="photo photo--historic-hotel" role="img" aria-label="Photo: restored historic arcaded building under a pink sunset sky"></div>

    <div class="logo">
      <span class="logo__mark" aria-hidden="true"></span>
      <span class="logo__name">HARROW VALE</span>
      <span class="logo__partners">+ PARTNERS</span>
      <span class="logo__services">ARCHITECTURE • INTERIOR DESIGN</span>
    </div>

    <div class="photo photo--lounge-interior" role="img" aria-label="Photo: bright lounge with blue sofa, rattan chairs and pendant lamp"></div>
    <div class="photo photo--bar-interior" role="img" aria-label="Photo: teal restaurant bar with patterned stools and pendant lights"></div>
    <div class="photo photo--car-showroom" role="img" aria-label="Photo: glass car showroom with palm trees and parked cars"></div>

    <div class="portfolio-band">
      <div class="photo photo--atrium-stair" role="img" aria-label="Photo: white atrium with glass staircase and feature wall"></div>
      <div class="photo photo--waterfront-condo" role="img" aria-label="Photo: white waterfront condominium framed by flowering trees"></div>
      <div class="photo photo--office-lounge" role="img" aria-label="Photo: open office lounge with hexagon ceiling panels"></div>
      <div class="photo photo--spanish-lobby" role="img" aria-label="Photo: lobby with carved wood ceiling, lantern and terracotta floor"></div>
    </div>

    <footer class="contact-bar">
      <span class="contact-bar__item">48 Coral Avenue, Port Sable, Florida</span>
      <span class="contact-bar__divider"></span>
      <span class="contact-bar__item contact-bar__item--phone">(555) 014-2290</span>
      <span class="contact-bar__divider"></span>
      <span class="contact-bar__item">HarrowVale.com</span>
    </footer>
  </section>
</main>
</body>
</html>
```